依頼詳細
当院がこの度4月より、木曜診療・駐車場提携・CT導入をしたため、そのお知らせのチラシを作成いただきたいです。(A4裏表)
ラフ・素材等はございます。HP(http://mk-dental.net/)取っていただいても構いません。

※発送はポミネオ様で行う予定です。(https://pomineo.com/directmail/large-sized-postcard/
※まず表面案だけで構いませんのでお出しいただけますと幸いです。その後当選の方が決まり次第裏面もお願いしようと思います。
記載項目
添付ラフ通り
サイズ
A4
ページ数
両面
希望イメージ
シンプル 複雑
単色 カラフル
暗い 明るい
日常 高級
遊び心 厳粛
未来的 伝統的
女性的 男性的
希望する色
緑系
納品ファイル
• イラストレーター形式 (.ai)
• PNG形式 (.png)
補足説明
ポミネオのDM(https://pomineo.com/directmail/large-sized-postcard/)で患者様に発送するため、ポミネオの規定で作成願えますでしょうか。
■ 選んだ理由

全体的なデザインバランスが良かったため

■ 提案者全員のお礼・コメント

この度はご参加いただきまして誠に有難うございました!
今後とも宜しくお願いいたします。

```html
<!DOCTYPE html>
<html lang="ja">
<head>
<meta charset="utf-8">
<title>花園町ファミリー歯科 お知らせ</title>
<link href="https://fonts.googleapis.com/css2?family=Noto+Sans+JP:wght@400;500;700;900&family=Noto+Serif+JP:wght@500;700&display=swap" rel="stylesheet">
<style>
:root{
  --green:#5fb236;
  --green-dark:#3d8a22;
  --green-deep:#2f6e1a;
  --green-pale:#e6f2d8;
  --green-soft:#cfe6b6;
  --yellow:#f4e64a;
  --ink:#333;
  --white:#fff;
}
*{box-sizing:border-box;margin:0;padding:0}
html,body{width:846px;height:1200px;overflow:hidden;background:#fff}
body{font-family:"Noto Sans JP",sans-serif;color:var(--ink)}
.flyer{position:relative;width:846px;height:1200px;overflow:hidden;background:var(--white)}

/* top notice */
.notice{position:absolute;left:0;top:0;width:846px;height:345px;background:var(--green)}
.notice-date{position:absolute;left:42px;top:26px;color:#fff;font-weight:900;font-size:44px;letter-spacing:1px}
.notice-head{position:absolute;left:42px;top:84px;color:#fff;font-weight:900;font-size:62px;letter-spacing:2px}
.notice-head .key{color:var(--yellow)}
.hours{position:absolute;top:196px}
.hours.old{left:28px;width:240px}
.hours.new{left:300px;width:520px}
.hours-label{font-size:14px;font-weight:700;color:var(--yellow);margin-bottom:6px}
.hours-label::before{content:"◆";margin-right:4px}
.hours table{width:100%;background:#fff;border-collapse:collapse;border-radius:6px;overflow:hidden}
.hours th,.hours td{border:1px solid var(--green-soft);text-align:center;font-size:10px;height:24px;color:var(--ink)}
.hours.new th,.hours.new td{font-size:20px;height:34px;font-weight:700;color:var(--green-dark)}
.hours.new th.time{font-size:12px;color:var(--ink);font-weight:500}
.dot{display:inline-block;width:10px;height:10px;border-radius:50%;background:var(--green)}
.hours.new .dot{width:18px;height:18px}
.x{color:#999}
.hours-note{font-size:10px;color:#fff;margin-top:5px}
.arrow{position:absolute;left:274px;top:250px;width:0;height:0;border-top:16px solid transparent;border-bottom:16px solid transparent;border-left:18px solid #fff}

/* parking */
.badge{position:absolute;left:48px;top:360px;width:160px;height:76px;border-radius:40px;background:var(--green);color:#fff;font-weight:700;font-size:17px;text-align:center;line-height:1.25;padding-top:16px}
.parking-title{position:absolute;left:225px;top:378px;font-size:36px;font-weight:900;color:var(--green-deep);display:flex;align-items:center;gap:10px}
.p-icon{width:38px;height:38px;background:var(--green);color:#fff;border-radius:4px;font-size:28px;text-align:center;line-height:38px}
.parking-rule{position:absolute;left:48px;top:440px;width:760px;height:3px;background:var(--green)}
.free{position:absolute;left:70px;top:480px;width:250px;height:310px;text-align:center;font-family:"Noto Serif JP",serif;color:var(--ink)}
.free .min{font-size:60px;font-weight:700;line-height:1.05}
.free .tilde{font-size:40px;line-height:.9}
.free .label{font-size:64px;font-weight:700;line-height:1.1}
.free .cond{display:inline-block;margin-top:14px;font-family:"Noto Sans JP",sans-serif;font-size:14px;border:1px solid var(--ink);border-radius:50%;padding:14px 12px;line-height:1.3}
.map{position:absolute;left:360px;top:460px;width:460px;height:390px;background:linear-gradient(135deg,#f2f2ee,#e4ece0);border-radius:4px}

/* CT */
.ct{position:absolute;left:0;top:880px;width:846px;height:320px;background:var(--green-pale)}
.ct-title{position:absolute;left:0;top:14px;width:460px;height:54px;background:var(--green-deep);color:#fff;font-size:32px;font-weight:900;padding-left:24px;line-height:54px}
.ct-photo{position:absolute;left:18px;top:86px;width:140px;height:222px;background:linear-gradient(180deg,#ffffff,#cfd6cc)}
.ct-merits{position:absolute;left:170px;top:86px;width:290px;height:222px;background:#fff;border-radius:4px;padding:10px 12px}
.ct-merits h3{font-size:14px;color:var(--green-deep);margin-bottom:6px}
.ct-merits li{list-style:none;font-size:10.5px;line-height:1.5;margin-bottom:4px;padding-left:14px;position:relative}
.ct-merits li::before{content:"";position:absolute;left:0;top:4px;width:9px;height:9px;background:var(--green);border-radius:2px}
.clinic{position:absolute;left:490px;top:96px;width:330px}
.clinic-name{display:flex;align-items:center;gap:10px;font-size:30px;font-weight:700;color:var(--green-deep)}
.clinic-name .mark{width:26px;height:26px;border-radius:50%;background:var(--green)}
.clinic-addr{margin-top:20px;font-size:14px;line-height:1.6}
.clinic-tel{margin-top:10px;font-size:34px;font-weight:900;color:var(--green-deep)}
</style>
</head>
<body>
<main class="flyer">
  <section class="notice">
    <p class="notice-date">4月1日より</p>
    <h1 class="notice-head"><span class="key">木曜日</span>の診療を開始します</h1>

    <div class="hours old">
      <p class="hours-label">今までの診療時間</p>
      <table>
        <tr><th>診療時間</th><th>月</th><th>火</th><th>水</th><th>木</th><th>金</th><th>土</th></tr>
        <tr><th>9:30〜13:00</th><td><span class="dot"></span></td><td><span class="dot"></span></td><td><span class="dot"></span></td><td class="x">×</td><td><span class="dot"></span></td><td><span class="dot"></span></td></tr>
        <tr><th>14:30〜19:00</th><td><span class="dot"></span></td><td><span class="dot"></span></td><td><span class="dot"></span></td><td class="x">×</td><td><span class="dot"></span></td><td><span class="dot"></span></td></tr>
      </table>
      <p class="hours-note">休診日：木曜日・日曜日・祝日</p>
    </div>
    <div class="arrow"></div>
    <div class="hours new">
      <p class="hours-label">4月1日からの診療時間</p>
      <table>
        <tr><th class="time">診療時間</th><th>月</th><th>火</th><th>水</th><th>木</th><th>金</th><th>土</th></tr>
        <tr><th class="time">9:30〜13:00</th><td><span class="dot"></span></td><td><span class="dot"></span></td><td><span class="dot"></span></td><td><span class="dot"></span></td><td><span class="dot"></span></td><td><span class="dot"></span></td></tr>
        <tr><th class="time">14:30〜19:00</th><td><span class="dot"></span></td><td><span class="dot"></span></td><td><span class="dot"></span></td><td><span class="dot"></span></td><td><span class="dot"></span></td><td><span class="dot"></span></td></tr>
      </table>
      <p class="hours-note">休診日：日曜日・祝日</p>
    </div>
  </section>

  <section class="parking">
    <div class="badge">ご来院がより<br>簡単に</div>
    <h2 class="parking-title"><span class="p-icon">P</span>駐車場サービスのご案内</h2>
    <div class="parking-rule"></div>
    <div class="free">
      <p class="min">40分</p>
      <p class="tilde">〜</p>
      <p class="min">60分</p>
      <p class="label">無料</p>
      <p class="cond">駐車場によって<br>変わります</p>
    </div>
    <div class="map" role="img" aria-label="医院周辺の地図と提携駐車場の位置"></div>
  </section>

  <section class="ct">
    <h2 class="ct-title">歯科用CT導入しました</h2>
    <div class="ct-photo" role="img" aria-label="歯科用CT装置の写真"></div>
    <div class="ct-merits">
      <h3>CTのメリット</h3>
      <ul>
        <li>立体的な画像で骨や神経の位置を正確に把握できます。</li>
        <li>インプラント治療の安全性が高まります。</li>
        <li>根の治療で病巣を見落としにくくなります。</li>
        <li>短時間の撮影で体への負担も少なく済みます。</li>
        <li>画像を見ながら分かりやすく説明します。</li>
      </ul>
    </div>
    <div class="clinic">
      <p class="clinic-name"><span class="mark"></span>花園町ファミリー歯科</p>
      <p class="clinic-addr">〒537-0024<br>大阪府大阪市東成区緑橋1-2-3</p>
      <p class="clinic-tel">TEL 06-6555-0192</p>
    </div>
  </section>
</main>
</body>
</html>
```